Flyer für eine Zahnarztpraxis
Zielgruppe
Zahnarztpraxis, Zielgruppe sind Patienten im Erwachsenenalter
Aufgabenstellung
Den Text habe ich bereits geschrieben. Es soll ein DINA4 Flyer werden, mit sechs Seiten.

```html
<!DOCTYPE html>
<html lang="de">
<head>
<meta charset="utf-8">
<title>Flyer Zahnarztpraxis – Vitamin D</title>
<link href="https://fonts.googleapis.com/css2?family=Outfit:wght@400;500;600;700&display=swap" rel="stylesheet">
<style>
:root{
  --yellow:#ebe700;
  --paper:#f6f1f3;
  --grey:#dcd8da;
  --mauve:#b9506f;
  --green:#3f6b5d;
  --ink:#1e1e1e;
  --bg:#9d9d9d;
}
*{box-sizing:border-box;margin:0;padding:0}
html,body{width:706px;height:1200px;overflow:hidden;background:var(--bg);font-family:"Outfit",sans-serif;color:var(--ink)}
.spread{position:absolute;left:13px;width:680px;height:481px;display:flex;box-shadow:0 6px 18px rgba(0,0,0,.25)}
.spread--outside{top:99px}
.spread--inside{top:620px}
.panel{position:relative;width:226.67px;height:100%;overflow:hidden}
.panel--paper{background:var(--paper)}
.panel--yellow{background:var(--yellow)}
.panel--grey{background:var(--grey)}
.photo{position:absolute}
h2{font-weight:600;line-height:1.1}
.rule{height:1.5px;background:var(--mauve);margin:6px 0 8px}
.ticks{list-style:none}
.ticks li{position:relative;padding-left:12px;font-size:7px;line-height:1.25;margin-bottom:5px}
.ticks li::before{content:"✓";position:absolute;left:0;top:1px;width:7px;height:7px;border-radius:50%;background:var(--mauve);color:#fff;font-size:5px;line-height:7px;text-align:center;font-weight:700}
p{font-size:7px;line-height:1.3}
.accent{color:var(--mauve);font-weight:600}
/* outside */
.situations{position:absolute;left:20px;right:18px;top:206px}
.situations h2{font-size:14px}
.situations .strong{font-weight:600;margin-top:8px}
.bottom-band{position:absolute;left:0;right:0;bottom:0;height:8px;background:var(--yellow)}
.worth{position:absolute;left:14px;right:14px;top:216px;text-align:center}
.worth h2{font-size:17px;margin-bottom:10px}
.worth p{font-weight:600;margin-bottom:8px}
.pill{display:inline-block;margin-top:8px;background:var(--mauve);color:#fff;font-size:8px;font-weight:500;padding:4px 9px;border-radius:3px}
.pill::before{content:"";display:inline-block;width:6px;height:6px;border-radius:50%;background:#fff;margin-right:4px;vertical-align:-0.5px}
.brand{position:absolute;left:0;right:0;top:0;height:57px;background:var(--grey);display:flex;align-items:center;padding-left:18px;gap:8px}
.brand-mark{width:18px;height:18px;border:1.5px solid var(--green);border-radius:50%}
.brand-name{color:var(--green);font-size:8.5px;line-height:1.15;font-weight:400;letter-spacing:.3px}
.cover-title{position:absolute;left:10px;right:10px;top:70px;text-align:center}
.cover-title h1{font-size:19px;font-weight:700;line-height:1.05}
.cover-title p{font-size:7.5px;line-height:1.2;margin-top:6px}
.cover-photo{left:14px;top:168px;width:140px;height:106px;border:3px solid var(--paper);border-radius:4px 30px 4px 4px;background:linear-gradient(180deg,#3f7fc4 0%,#8fb8dd 55%,#6c8aa2 100%)}
.cover-photo--small{left:100px;top:244px;width:72px;height:62px;border-radius:4px 20px 4px 4px;background:linear-gradient(135deg,#e9d7c4,#c9a98a)}
.cover-question{position:absolute;left:20px;top:336px;width:130px;font-size:8.5px;font-weight:600;line-height:1.15}
.teaser{position:absolute;left:10px;right:0;bottom:0;height:52px;background:var(--mauve);color:var(--paper);border-radius:8px 0 0 0;padding:10px 12px;font-size:10.5px;font-weight:600;line-height:1.1}
/* inside */
.whatis{position:absolute;left:20px;right:16px;top:24px}
.whatis h2{font-size:14px}
.whatis p{margin-bottom:7px}
.why{position:absolute;left:20px;right:14px;top:292px}
.why h2{font-size:14px}
.why .rule{width:110px;background:var(--ink);height:1px}
.why p{margin-top:8px}
.connect{position:absolute;left:18px;right:16px;top:28px}
.connect h2{font-size:14px}
.callout{background:var(--mauve);color:#fff;font-size:7.5px;font-weight:600;line-height:1.15;padding:5px 8px;border-radius:4px;margin:8px 0}
.connect .lead{font-weight:600;margin:6px 0 5px}
.risks{list-style:none}
.risks li{display:flex;align-items:center;gap:8px;font-size:7px;line-height:1.2;margin-bottom:6px}
.risks svg{flex:none}
.dots{position:absolute;right:12px;top:10px}
</style>
</head>
<body>

<section class="spread spread--outside">
  <div class="panel panel--paper">
    <div class="photo" role="img" aria-label="Hand hält Pipettenfläschchen mit Vitamin-D-Öl vor sonnigem Himmel" style="left:0;top:0;width:100%;height:185px;background:linear-gradient(160deg,#8fb3d6 0%,#dfe8f1 45%,#f3e2c9 70%,#c88d72 100%)"></div>
    <div class="situations">
      <h2>Kennen Sie diese<br>Situationen?</h2>
      <div class="rule" style="width:120px"></div>
      <ul class="ticks">
        <li>Kommen Sie seltener an die frische Luft, als Sie es sich wünschen?</li>
        <li>Fühlen Sie sich häufig antriebslos oder niedergeschlagen, besonders in den Wintermonaten?</li>
        <li>Haben Sie gelegentlich empfindliche Zähne oder Zahnfleischprobleme?</li>
      </ul>
      <p class="strong">Vielleicht steckt hinter Ihren Beschwerden ein Vitamin-D-Mangel. Mit einem Bluttest in unserer Praxis, können wir herausfinden, ob Ihrem Körper etwas fehlt</p>
      <p class="strong">– und unterstützen Sie bei der passenden Ergänzung.</p>
    </div>
    <div class="bottom-band"></div>
  </div>

  <div class="panel panel--yellow">
    <div class="photo" role="img" aria-label="Hände formen ein Herz vor der untergehenden Sonne über einer Wiese" style="left:0;top:0;width:100%;height:180px;border-radius:0 0 40px 0;background:linear-gradient(180deg,#c98a4a 0%,#f4d27a 40%,#a59a4a 70%,#4c6a2c 100%)"></div>
    <div class="worth">
      <h2>Ihr Lächeln und<br>Ihre Gesundheit<br>sind es wert!</h2>
      <p>Vitamin D ist ein wichtiger Baustein<br>für ein gesundes Leben – und<br>gesunde Zähne.</p>
      <p>Unser Praxisteam berät Sie gern persönlich<br>und beantwortet Ihre Fragen.</p>
      <p>Kommen Sie einfach auf uns zu –<br>für Ihre Gesundheit von Kopf bis Fuß.</p>
      <span class="pill">zahnarztpraxis-lindhoff.de</span>
    </div>
  </div>

  <div class="panel panel--yellow">
    <div class="brand">
      <span class="brand-mark"></span>
      <span class="brand-name">ZAHNARZTPRAXIS<br>LINDHOFF &amp; TEAM</span>
    </div>
    <div class="cover-title">
      <h1>Vitamin D -<br>mehr als nur ein<br>Sonnenvitamin</h1>
      <p>Was Ihre Zähne und Ihr Körper jetzt<br>brauchen könnten</p>
    </div>
    <div class="photo cover-photo" role="img" aria-label="Junge Frau mit Kopfhörern sitzt entspannt in der Sonne"></div>
    <div class="photo cover-photo cover-photo--small" role="img" aria-label="Lachendes Kind"></div>
    <div class="cover-question">Fühlen Sie sich<br>oft müde? Haben<br>Sie manchmal<br>Zahnfleischprobleme oder<br>empfindliche Zähne?</div>
    <div class="teaser">Vielleicht steckt mehr<br>dahinter, als Sie denken...</div>
  </div>
</section>

<section class="spread spread--inside">
  <div class="panel panel--grey">
    <div class="whatis">
      <h2>Was ist Vitamin D<br>eigentlich?</h2>
      <div class="rule" style="width:120px"></div>
      <p>Vitamin D wird oft „Sonnenvitamin“ genannt, weil unser Körper es größtenteils selbst bildet – wenn Sonne auf unsere Haut trifft.</p>
      <p><span class="accent">Doch:</span> In unseren Breitengraden reicht die Sonnenstrahlung viele Monate im Jahr nicht aus, um genügend Vitamin D zu bilden.</p>
      <p><span class="accent">Wissen Sie wo Sie stehen?</span> Gemeinsam können wir Ihren Vitamin D Spiegel in wenigen Minuten bestimmen.</p>
    </div>
    <div class="photo" role="img" aria-label="Frau genießt mit geschlossenen Augen die Sonne am See" style="left:0;top:200px;width:100%;height:281px;border-radius:0 40px 0 0;background:linear-gradient(180deg,#2f5d6e 0%,#6c8c8f 45%,#b88f7c 75%,#7c5045 100%)"></div>
  </div>

  <div class="panel panel--yellow">
    <div class="photo" role="img" aria-label="Gruppe lachender Erwachsener klatscht sich beim Sport ab" style="left:12px;top:22px;width:200px;height:232px;border:4px solid var(--paper);border-radius:6px 50px 6px 50px;background:linear-gradient(180deg,#6f8a5a 0%,#a9b58a 35%,#d7c6b2 60%,#5a6a8a 100%)"></div>
    <div class="why">
      <h2>Warum ist Vitamin D so<br>wichtig für den Körper?</h2>
      <div class="rule"></div>
      <ul class="ticks">
        <li>Unterstützt ein starkes Immunsystem</li>
        <li>Trägt zu kräftigen Knochen bei</li>
        <li>Fördert Muskelfunktion und Gleichgewicht</li>
        <li>Kann Müdigkeit und Antriebslosigkeit entgegenwirken</li>
      </ul>
      <p>Fehlt Vitamin D, kann das langfristig Auswirkungen auf viele Bereiche unserer Gesundheit haben – oft, ohne dass wir es sofort merken.</p>
    </div>
  </div>

  <div class="panel panel--paper">
    <svg class="dots" width="14" height="20" viewBox="0 0 14 20" aria-hidden="true">
      <g fill="#9a9a9a"><circle cx="1" cy="1" r="0.9"/><circle cx="7" cy="1" r="0.9"/><circle cx="13" cy="1" r="0.9"/><circle cx="1" cy="10" r="0.9"/><circle cx="7" cy="10" r="0.9"/><circle cx="13" cy="10" r="0.9"/><circle cx="1" cy="19" r="0.9"/><circle cx="7" cy="19" r="0.9"/><circle cx="13" cy="19" r="0.9"/></g>
    </svg>
    <div class="connect">
      <h2>Vitamin D und Ihre<br>Zähne – eine starke<br>Verbindung</h2>
      <div class="callout">Wussten Sie, dass Vitamin D<br>entscheidend für gesunde Zähne ist?</div>
      <p>Es sorgt dafür, dass Kalzium im Körper optimal aufgenommen wird – und Kalzium ist der Baustoff für feste Zähne und stabilen Kieferknochen.</p>
      <p class="lead">Ein Mangel kann unter anderem begünstigen:</p>
      <ul class="risks">
        <li><svg width="12" height="12" viewBox="0 0 12 12"><path d="M2 3c1-2 3-1 4 0 1-1 3-2 4 0 1 2-1 4-1 7-1 1-2 0-2-2 0-1-2-1-2 0 0 2-1 3-2 2 0-3-2-5-1-7z" fill="none" stroke="var(--green)" stroke-width="1"/></svg>Zahnfleischprobleme</li>
        <li><svg width="12" height="12" viewBox="0 0 12 12"><path d="M2 3c1-2 3-1 4 0 1-1 3-2 4 0 1 2-1 4-1 7-1 1-2 0-2-2 0-1-2-1-2 0 0 2-1 3-2 2 0-3-2-5-1-7z" fill="none" stroke="var(--green)" stroke-width="1"/></svg>Lockerung der Zähne</li>
        <li><svg width="12" height="12" viewBox="0 0 12 12"><path d="M2 2h8v3H2z M4 5h4v1H4z M5 6h2v5H5z" fill="var(--green)"/></svg>Schlechte Einheilung von Implantaten</li>
        <li><svg width="12" height="12" viewBox="0 0 12 12"><path d="M2 3c1-2 3-1 4 0 1-1 3-2 4 0 1 2-1 4-1 7-1 1-2 0-2-2 0-1-2-1-2 0 0 2-1 3-2 2 0-3-2-5-1-7z" fill="var(--green)"/></svg>Verzögerte Heilung nach zahnärztlichen Eingriffen</li>
      </ul>
    </div>
    <div class="photo" role="img" aria-label="Lachendes Seniorenpaar im herbstlichen Park" style="left:0;top:308px;width:100%;height:173px;border-radius:40px 0 0 0;background:linear-gradient(135deg,#d9a52a 0%,#f0c95a 40%,#b4824a 70%,#7a3b3b 100%)"></div>
  </div>
</section>

</body>
</html>
```